I need a cover for a brochure made

I need a cover for a brochure. The dimensions are 8.25 wide and 5.25 high... I also need a .25 inch bleed outside of those dimensions.

I need it to look like a vintage photo album cover. In big words, I would like it to say "Family". Above it in smaller words "To our Harlow Fairway" ... making it look like the words are gold inlay or something.

I would like it kind of in the style of some of the attached maybe. Just vintage looking.

```html
<!DOCTYPE html>
<html lang="en">
<head>
<meta charset="utf-8">
<title>Family – Harlow Fairway Brochure Cover</title>
<link href="https://fonts.googleapis.com/css2?family=Cinzel:wght@400&display=swap" rel="stylesheet">
<style>
  :root {
    --leather-light: #8c4228;
    --leather-mid: #73311d;
    --leather-dark: #521f11;
    --leather-spot: #9a4a2c;
    --gold: #f2c12e;
    --gold-mid: #d9a228;
    --gold-deep: #a87418;
    --gold-shadow: #2e1005;
    --subtitle-gold: #b9832a;
  }
  html, body {
    margin: 0;
    padding: 0;
    width: 1200px;
    height: 764px;
    overflow: hidden;
    background: var(--leather-mid);
  }
  .cover {
    position: relative;
    width: 1200px;
    height: 764px;
    overflow: hidden;
    background:
      radial-gradient(ellipse 420px 260px at 30% 30%, rgba(154,74,44,0.45), rgba(154,74,44,0) 70%),
      radial-gradient(ellipse 380px 240px at 70% 62%, rgba(154,74,44,0.35), rgba(154,74,44,0) 70%),
      radial-gradient(ellipse 300px 200px at 55% 85%, rgba(82,31,17,0.35), rgba(82,31,17,0) 70%),
      radial-gradient(ellipse at 50% 45%, var(--leather-light) 0%, var(--leather-mid) 60%, var(--leather-dark) 100%);
  }
  .frame {
    position: absolute;
    inset: 0;
    width: 1200px;
    height: 764px;
  }
  .frame-line {
    stroke: var(--gold);
    stroke-width: 2;
    fill: none;
  }
  .frame-dots {
    stroke: var(--gold);
    stroke-width: 3.5;
    stroke-linecap: round;
    stroke-dasharray: 0 11;
    fill: none;
  }
  .corner-ornament {
    fill: url(#ornamentTone);
    stroke: var(--gold);
    stroke-width: 2;
  }
  .title-block {
    position: absolute;
    left: 0;
    right: 0;
    top: 320px;
    text-align: center;
    font-family: "Cinzel", serif;
  }
  .title-main {
    margin: 0;
    font-weight: 400;
    font-size: 106px;
    line-height: 1;
    letter-spacing: 2px;
    color: var(--gold);
    text-shadow: 1px 1px 0 var(--gold-deep), 2px 3px 3px var(--gold-shadow);
  }
  .title-sub {
    margin: -10px 0 0;
    font-weight: 400;
    font-size: 28px;
    line-height: 1;
    letter-spacing: 0.5px;
    color: var(--subtitle-gold);
    text-shadow: 1px 1px 2px var(--gold-shadow);
  }
</style>
</head>
<body>
  <main class="cover">
    <svg class="frame" viewBox="0 0 1200 764" aria-hidden="true">
      <defs>
        <linearGradient id="ornamentTone" x1="0" y1="0" x2="1" y2="1">
          <stop offset="0" stop-color="#d9a228" stop-opacity="0.85"/>
          <stop offset="1" stop-color="#8f5a1c" stop-opacity="0.55"/>
        </linearGradient>
      </defs>
      <line class="frame-line" x1="285" y1="39" x2="915" y2="39"/>
      <line class="frame-dots" x1="300" y1="49" x2="900" y2="49"/>
      <line class="frame-dots" x1="300" y1="716" x2="900" y2="716"/>
      <line class="frame-line" x1="285" y1="726" x2="915" y2="726"/>
      <line class="frame-line" x1="22" y1="255" x2="22" y2="510"/>
      <line class="frame-line" x1="1178" y1="255" x2="1178" y2="510"/>
    </svg>

    <svg class="frame" viewBox="0 0 1200 764">
      <g role="img" aria-label="Gold filigree scrollwork corner ornament, top left">
        <path class="corner-ornament" d="M18 18 H285 V62 Q120 70 72 250 H18 Z"/>
      </g>
      <g role="img" aria-label="Gold filigree scrollwork corner ornament, top right" transform="translate(1200 0) scale(-1 1)">
        <path class="corner-ornament" d="M18 18 H285 V62 Q120 70 72 250 H18 Z"/>
      </g>
      <g role="img" aria-label="Gold filigree scrollwork corner ornament, bottom left" transform="translate(0 764) scale(1 -1)">
        <path class="corner-ornament" d="M18 18 H285 V62 Q120 70 72 250 H18 Z"/>
      </g>
      <g role="img" aria-label="Gold filigree scrollwork corner ornament, bottom right" transform="translate(1200 764) scale(-1 -1)">
        <path class="corner-ornament" d="M18 18 H285 V62 Q120 70 72 250 H18 Z"/>
      </g>
    </svg>

    <div class="title-block">
      <h1 class="title-main">FAMILY</h1>
      <p class="title-sub">TO OUR HARLOW FAIRWAY</p>
    </div>
  </main>
</body>
</html>
```